Catalogue for Eco friendly products

HI We have 2 brands - logos attached
Verdatotenz
Lumawrap

We would like a catalog of these products :

Size of the catalogue: A4 Size

Verdatote - ( www.verdatote.co.nz)
Cotton bags
Canvas bags
Jute bags
Non woven bags
Mudwiser poop bags

Lumawrap
Degradable bin liners
Compostable bin liners
Recycled bin liners
Paper bags
Customised packaging

All products need to be on A4 page which can be inserted in a folder, the main reason for that to make sales presentation as per the customer requirement. All customers don't need all the products.

We are looking for the designer to make a clean feel where both the logos sit comfortably with each other.

We will need 2 main designs:
1 will be the outside folder design
Inside Catalog for the products with place holders for the photographs and words which can be limited to 10-20 words to ensure that design looks uniform. All products are on our website to provide you with an idea of what we are looking for.

Lumawrap packaging logo is included for your reference to get a feel of the products.
Any other information please let me know.
Thanks

Target Market(s)

B2B- Businesses , purchase manager , event managers, Organic shop owners

Font styles to use
Serif
Sans Serif

Colors
add136
abd037
acd037
cadf82
9bcb3c
f37122

Requirements
Must have
• A Clean design and yet interesting , use of green colour is preferred for the design but complimentary earthy colors are ok
• TEXT in design: Attached for 1 product category : Cotton
Nice to have
• Please see the design inspirations which I like. Please note that these are just to give you an idea of what kind of design we would prefer and is to be used as our guidance to you.

```html
<!DOCTYPE html>
<html lang="en">
<head>
<meta charset="utf-8">
<title>Fairshare Bag – Verdatote NZ</title>
<link href="https://fonts.googleapis.com/css2?family=Montserrat:wght@300;400&display=swap" rel="stylesheet">
<style>
  :root {
    --paper: #ffffff;
    --paper-tint: #e9ecdc;
    --ink: #5a5a5a;
    --ink-soft: #6e6e6e;
    --accent-orange: #f37122;
    --leaf: #9bcb3c;
    --band: #cadf82;
    --badge: #1f1f1f;
    --bag-light: #f1ece0;
    --bag-shade: #ddd5c3;
  }
  * { margin: 0; padding: 0; box-sizing: border-box; }
  html, body { width: 794px; height: 1200px; overflow: hidden; }
  body { font-family: "Montserrat", sans-serif; color: var(--ink); }
  .page {
    position: relative;
    width: 794px; height: 1200px;
    background: radial-gradient(ellipse 900px 700px at 100% 0%, var(--paper-tint) 0%, #f4f5ee 40%, var(--paper) 75%);
    overflow: hidden;
  }
  .product-photo {
    position: absolute; left: 308px; top: 100px; width: 184px; height: 360px;
    background: linear-gradient(160deg, var(--bag-light) 0%, var(--bag-shade) 100%);
    border-radius: 4px;
  }
  .product-title {
    position: absolute; top: 484px; left: 0; width: 100%;
    text-align: center; font-weight: 400; font-size: 34px; color: var(--accent-orange);
  }
  .copy { position: absolute; left: 89px; width: 617px; top: 530px; font-weight: 300; }
  .copy h2 { font-size: 18px; font-weight: 300; line-height: 30px; }
  .copy p { font-size: 18px; line-height: 33.8px; text-align: justify; }
  .copy p + p { margin-top: 15px; }
  .spec { position: absolute; left: 89px; top: 994px; font-size: 12px; line-height: 19px; font-weight: 300; color: var(--ink-soft); }
  .cert-badge { position: absolute; left: 62px; top: 1080px; width: 56px; height: 32px; background: var(--badge); }
  .brand {
    position: absolute; left: 622px; top: 1082px; display: flex; align-items: center; gap: 6px;
    font-size: 22px; font-weight: 300; color: var(--leaf);
  }
  .brand .mark { width: 22px; height: 22px; border: 2px solid var(--leaf); }
  .footer-band { position: absolute; left: 0; bottom: 0; width: 100%; height: 76px; background: var(--band); }
</style>
</head>
<body>
<div class="page">
  <div class="product-photo" role="img" aria-label="Natural calico tote bag with long handles and a small printed event graphic"></div>

  <h1 class="product-title">Fairshare Bag</h1>

  <section class="copy">
    <h2>What is Fairshare?</h2>
    <p>Fairshare is about better prices, decent working conditions, local sustainability, and fair terms of trade for farmers and workers in the developing world. By requiring companies to pay sustainable prices (which must never fall lower than the market price), Fairshare addresses the injustices of conventional trade, which traditionally discriminates against the poorest, weakest producers. It enables them to improve their position and have more control over their lives.</p>
    <p>Verdatote NZ is certified as fairshare supplier for Calico &amp; Canvas bags , these unprinted bags come with our FSO ID for your peace of mind that you are buying a certified Fairshare bag.</p>
  </section>

  <div class="spec">
    In Stock – Unprinted<br>
    SKU: Fairshare. Category: Calico Cotton. Tags: calico, cotton, fairshare, natural, tote.<br>
    Size: 36.5cm(w) X 39cm(h) X 8.5cm(g)
  </div>

  <div class="cert-badge" aria-hidden="true"></div>
  <div class="brand"><span>Verdatotenz</span><span class="mark" aria-hidden="true"></span></div>

  <div class="footer-band"></div>
</div>
</body>
</html>
```